Cedar Hollow Resort & Marina - Boat Slips, Cabin Rentals, Floating Vacation Homes, & More

We need an 8'H x 16'W billboard for our Resort & marina, www.cedarhollowresort.example. We'd like it to include: Lakefront Cabin Rentals, Floating Vacation Homes, and New Slips Summer 2022. We'd like it to be simple using the colors on our logo, similar to our business cards, and have our logo on it large. Maybe an arrow on the bottom pointing left that says 3 miles, possibly our website and phone number.

Target Market(s)

Lake People, Boaters

Industry/Entity Type

Resort & Marina (Recreation/Hospitality)

Font styles to use
Sans Serif
Other font styles liked:
• Simple/modern

Colors
0054AA
0677BA
7BADD7
CADEEF
E8F1F8
FFC000
F8CF3A
FAE287
FDF2CF
FEFAEE
F0912C
F2A743
F7CA91
FBE8D2
FDF5EE

Requirements
Must have
• Logo, Cabin Rentals, Floating Vacation Homes, New Slips Summer 2022
Nice to have
• An additional banner hanging from the bottom with an orange (or blue, colors from our logo) arrow pointing left, with white text saying: 3 miles 555-214-6873 www.cedarhollowresort.example
Should not have
• Shouldn't be too busy

```html
<!DOCTYPE html>
<html lang="en">
<head>
<meta charset="utf-8">
<title>Cedar Hollow Resort & Marina Billboard</title>
<link href="https://fonts.googleapis.com/css2?family=Montserrat:wght@500;600;700&display=swap" rel="stylesheet">
<style>
  :root {
    --navy: #1a4178;
    --orange: #f5a623;
    --yellow: #ffd200;
    --white: #ffffff;
    --panel: #f4f5f7;
    --backdrop: #d4d4d4;
  }
  * { box-sizing: border-box; margin: 0; padding: 0; }
  html, body { width: 941px; height: 1200px; overflow: hidden; }
  body {
    background: var(--backdrop);
    font-family: "Montserrat", sans-serif;
    position: relative;
  }
  .billboard {
    position: absolute;
    left: 40px;
    top: 385px;
    width: 861px;
    height: 430px;
    background: var(--panel);
    overflow: hidden;
  }
  .billboard-shapes { position: absolute; inset: 0; }
  .offer-list {
    position: absolute;
    left: 29px;
    top: 26px;
    padding-left: 14px;
    border-left: 2px solid var(--orange);
    color: var(--white);
    font-weight: 700;
    font-size: 26px;
    line-height: 36px;
    letter-spacing: 0.3px;
    list-style: none;
  }
  .lake-map {
    position: absolute;
    left: 508px;
    top: 20px;
    width: 333px;
    height: 293px;
    background: radial-gradient(ellipse at 55% 55%, rgba(26,65,120,0.35), rgba(26,65,120,0.08) 70%, transparent 75%);
  }
  .lake-name {
    position: absolute;
    left: 604px;
    top: 84px;
    color: var(--navy);
    font-weight: 600;
    font-size: 17px;
  }
  .location-pin { position: absolute; left: 656px; top: 254px; }
  .address {
    position: absolute;
    left: 687px;
    top: 260px;
    color: var(--navy);
    font-weight: 500;
    font-size: 10.5px;
    line-height: 14px;
  }
  .brand {
    position: absolute;
    left: 230px;
    top: 200px;
    width: 360px;
    text-align: center;
    color: var(--navy);
    font-weight: 700;
  }
  .brand-mark {
    display: block;
    width: 58px;
    height: 58px;
    margin: 0 auto 10px;
    border-radius: 50%;
    background: var(--orange);
  }
  .brand-name { font-size: 36px; line-height: 40px; letter-spacing: 0.5px; }
  .brand-tag { font-size: 15px; letter-spacing: 6px; margin-top: 4px; }
  .direction-band {
    position: absolute;
    left: 0;
    top: 330px;
    width: 861px;
    height: 100px;
    background: var(--navy);
  }
  .direction-arrow { position: absolute; left: 22px; top: 14px; }
  .distance {
    position: absolute;
    left: 99px;
    top: 18px;
    font-weight: 700;
    font-size: 46px;
    line-height: 60px;
    color: var(--yellow);
  }
  .distance-number { color: var(--white); }
  .direction-flag { position: absolute; left: 306px; top: 31px; }
  .phone {
    position: absolute;
    left: 387px;
    top: 2px;
    font-weight: 700;
    font-size: 57px;
    line-height: 66px;
    color: var(--yellow);
    letter-spacing: 0.5px;
  }
  .website {
    position: absolute;
    left: 389px;
    top: 64px;
    font-weight: 600;
    font-size: 24px;
    line-height: 28px;
    color: var(--yellow);
  }
</style>
</head>
<body>
  <section class="billboard">
    <svg class="billboard-shapes" width="861" height="430" viewBox="0 0 861 430">
      <path fill="var(--navy)" d="M0 0 H681 C600 40 480 150 300 182 C180 200 80 178 0 163 Z"/>
      <path fill="var(--orange)" d="M0 170 C100 190 230 198 300 186 C345 178 385 162 411 146 C370 176 300 200 210 204 C130 207 60 198 0 190 Z"/>
    </svg>

    <ul class="offer-list">
      <li>NEW Slips 2022</li>
      <li>Floating Vacation Homes</li>
      <li>Lakefront Cabin Rentals</li>
    </ul>

    <div class="lake-map" role="img" aria-label="Map outline of Lake Texoma showing the resort location"></div>
    <div class="lake-name">Lake Texoma</div>
    <svg class="location-pin" width="22" height="30" viewBox="0 0 22 30">
      <path fill="var(--orange)" d="M11 0 C17 0 22 5 22 11 C22 18 11 30 11 30 C11 30 0 18 0 11 C0 5 5 0 11 0 Z"/>
    </svg>
    <p class="address">418 Cedar Hollow Road,<br>Lakeview, Texas 75000</p>

    <div class="brand">
      <span class="brand-mark"></span>
      <div class="brand-name">CEDAR HOLLOW</div>
      <div class="brand-tag">RESORT &amp; MARINA</div>
    </div>

    <div class="direction-band">
      <svg class="direction-arrow" width="66" height="74" viewBox="0 0 66 74">
        <path fill="var(--orange)" d="M0 37 L36 0 V20 H66 V54 H36 V74 Z"/>
      </svg>
      <div class="distance"><span class="distance-number">3</span> MILES</div>
      <svg class="direction-flag" width="52" height="40" viewBox="0 0 52 40">
        <path fill="var(--orange)" d="M0 0 H52 L40 20 L52 40 H0 Z"/>
      </svg>
      <div class="phone">555-214-6873</div>
      <div class="website">www.cedarhollowresort.example</div>
    </div>
  </section>
</body>
</html>
```